Lawn Bowls Travel Package Flyer and Poster

We are a New Zealand Travel Company and need a flyer to promote our Lawn Bowls Tours to 3 Destination for our customers... 1) Brochure Size is A4 and with a tri fold design 2) Also a poster A4 Size to be placed in the bowls club to promote our tours and destinations with contact details Outside Page Info Page 1 – Picture(s) overview Page 2 Intro Our winters bowls tours offer a chance to join a like-minded group of friends and bowling enthusiasts for the unique lawn bowls experience. All three tours are fully hosted and include return flights, quality accommodation, numerous groups meals, sightseeing activities, bowls fees plus much more these are a fantastic bowling tours that will truly bowl you over!. Non bowlers are very welcome on all tours as the bowls component is only part the total tour experience. Tour Manager and Bowls Ambassador Peter Holloway is an avid bowler and member of the Kestrel Ridge Bowling Club. Peter has been a European Tour Manager, Cruise Director and is an all-round good guy. Most recently as Silverfern Party Journeys Bowls Ambassador he has help design our last 8 Winter Tours and leads our bowling tours. His experience, assistance, wit and knowledge will ensure that you all have a great deal of fun on tour. Sightseeing & Meals All tours include pre-booked admissions to extensive and diverse range of the most popular sightseeing attractions in all destinations. Along with a number of group meals so the group can enjoy some culinary delights and opportunities to socialise. You're never alone and non-bowlers welcome We know that this Bowling holiday is a great way to meet new people and make new friends so we encourage those travelling solo to join us! Of course, you will have a guaranteed single room when you purchase the single price, however if you prefer not to pay the additional fee, we will match you with another single traveller of the same gender on a shared basis. Occasionally there will be an instance where there are no other single guests and in these cases you will have to pay the single supplement. Whilst we do try our best to match roommates, compatibility cannot be guaranteed and this offer is conditional on acceptance of this factor. Pre or Post Touring We are able to accommodate individuals who are wishing to see more of the destination either before or after the Tour – please contact us to discuss your touring requirements. Page 3 - Contact details Contact us today for a more details itinerary on all or any of the above tours Contact Details Silverfern Party Journeys PO Box 51-904 Wellington Mail Centre Website - www.silverfernpartyjourneys.example Email – bowls@silverfernpartyjourneys.example Freephone Phone – 0800 952 314 M 027 830 4726 Inside Pages Page 1 Tour 1 – Niue Dates – 19 June – 27 June 2020 About Niue is a Pacific paradise located north east of New Zealand and is just a 3 ½ hour flight from Auckland. One of the smallest countries, and one of the largest raised coral atolls on earth. Niue is a place where it’s normal for complete strangers to wave at each other, all the time. It’s a place where nature hasn’t been broken… and things are ‘The way they used to be’. Come and enjoy our beautiful little island. Make history and join us on at the first bowls week to held in Niue will included 3 days of bowls on Niue during the week along with a number of sightseeing activities on the Island Small Picture of bowls club Price from $ x twin/double share Page 2 Tour 2 - Norfolk Island Dates – 06 August -14 August 2020 Price from $x twin/double share About Norfolk Island is a popular lawn bowls destination, unlike some clubs in Australia and New Zealand the Norfolk greens remain open all year round. With recent reintroduce of direct from New Zealand we are delighted to offer a Tour to Norfolk Island where the locals are very welcoming to New Zealand to their greens. This is the bowls week to held will included 3 days of bowls during the week with a number of sightseeing activities on the island. Also for those wishing to extend onwards we are offering the option to combine with our Golden Sands Tour with a flight from Norfolk to Brisbane Small Picture Page 3 Tour 3 - Sunshine Coast Dates – 15 August – 23 August 2020 The Sunshine Coast our most popular tour with stunning winter climate, so join us for all that Queensland has to offer, this is a fantastic bowling tour that will truly bowl you over! An opportunity for you to experience some special events and enjoy the culture, sights, and foods, wines/beers or course some bowls This bowls week will included 3 days of bowls at different bowls clubs during the week with a number of sightseeing activities on the Sunshine Coast. Price from twin/double share Picture or logo Lawn Bowls
Target Market(s)
Lawn Bowlers in New Zealand for Winter Bowls Tour
Industry/Entity Type
Travel
Colors
Designer to choose colors to be used in the design.
Look and feel

```html
<!DOCTYPE html>
<html lang="en">
<head>
<meta charset="utf-8">
<title>Silverfern Party Journeys – Winter Bowls Tours Tri-fold</title>
<link href="https://fonts.googleapis.com/css2?family=Montserrat:wght@300;400;500;600;700;800&family=Arimo:wght@400;700&display=swap" rel="stylesheet">
<style>
  :root{
    --ink:#0a0a0a;
    --paper:#ffffff;
    --paper-shade:#e4e4e6;
    --backdrop:#c9c9cd;
    --grass:#5e6b3c;
    --sky:#d9c7c4;
    --foliage:#3f5a2e;
    --lake:#3f6a93;
    --spray:#c9cdd2;
    --boat:#d8a127;
  }
  *{box-sizing:border-box;margin:0;padding:0}
  html,body{width:1200px;height:2800px;overflow:hidden}
  body{background:var(--backdrop);position:relative;font-family:"Montserrat",sans-serif;color:var(--ink)}
  .spread{position:absolute;left:34px;width:1133px;height:801px;overflow:hidden;box-shadow:0 4px 14px rgba(0,0,0,.25)}
  .spread--outside{top:520px}
  .spread--inside{top:1460px}
  .spread__art{position:absolute;inset:0;width:1133px;height:801px}
  .abs{position:absolute}

  /* brand name lockup */
  .brand{font-family:"Montserrat",sans-serif;font-weight:700;text-align:center;line-height:1.1;letter-spacing:.5px}
  .brand--light{color:var(--paper)}
  .brand--dark{color:var(--ink)}

  /* outside: intro panel */
  .intro{left:36px;top:56px;width:282px;color:var(--paper);font-family:"Arimo",sans-serif;font-size:9.6px;line-height:12.4px;text-align:justify}
  .intro__kicker{font-family:"Montserrat",sans-serif;font-weight:300;font-size:26px;line-height:32px;text-align:left}
  .intro__title{font-family:"Montserrat",sans-serif;font-weight:700;font-size:26px;line-height:32px;margin-bottom:6px;text-align:left}
  .intro p{margin-bottom:14px}
  .intro__label{font-weight:700;font-size:9.6px;margin-bottom:3px}
  .intro__name{font-family:"Montserrat",sans-serif;font-weight:700;font-style:italic;font-size:14px}
  .intro__heading{font-family:"Montserrat",sans-serif;font-weight:600;font-size:14px;line-height:16px;text-align:left}
  .intro__cta{font-family:"Montserrat",sans-serif;font-weight:600;font-size:14px;line-height:16px;margin-top:-10px}

  /* outside: contact panel */
  .contact{left:377px;top:408px;width:378px;text-align:center}
  .contact__title{font-weight:700;font-size:23px;line-height:28px}
  .contact__sub{font-size:15px;line-height:18px;display:inline-block;border-bottom:2px solid var(--ink);padding:0 8px 6px}
  .contact__phone{font-weight:700;font-size:18px;line-height:30px}
  .contact__phones{margin-top:12px;margin-bottom:18px}
  .contact__line{font-size:10px;line-height:23px}
  .contact__brand{margin-top:36px;font-size:24px}

  /* outside: cover panel */
  .cover-logo{left:820px;top:0;width:249px;height:173px;background:var(--ink);display:flex;align-items:center;justify-content:center;padding:0 16px}
  .cover-logo .brand{font-size:22px}
  .cover{left:755px;top:600px;width:378px;text-align:center;color:var(--paper)}
  .cover__title{font-weight:700;font-size:48px;line-height:52px}
  .cover__sub{font-weight:700;font-size:32px;line-height:38px}
  .cover__tag{font-weight:400;font-size:21px;line-height:30px;margin-top:2px}
  .cover__url{display:inline-block;background:var(--paper);color:var(--ink);font-size:18px;line-height:24px;padding:0 8px;border-radius:5px;margin-top:10px}

  /* inside: tour panels */
  .tour{width:282px}
  .tour--light{color:var(--paper)}
  .tour--dark{color:var(--ink)}
  .tour__tag{display:inline-block;font-weight:300;font-size:25px;line-height:40px;padding:0 14px;border:1.5px solid currentColor}
  .tour__place{font-weight:700;font-size:22px;line-height:26px;margin-top:14px}
  .tour__dates{display:inline-block;font-weight:700;font-size:16px;line-height:22px;padding:0 6px;border-radius:4px;margin-top:6px}
  .tour--light .tour__dates{background:var(--paper);color:var(--ink)}
  .tour--dark .tour__dates{background:var(--ink);color:var(--paper)}
  .tour__about{font-family:"Arimo",sans-serif;font-size:12.2px;line-height:16.2px;text-align:justify;margin-top:26px}
  .tour__price-label{font-weight:700;font-size:12px;margin-top:18px}
  .tour__price{font-size:17px;line-height:32px}
  .tour__price b{font-size:30px;font-weight:700;margin-right:4px}

  .partner-box{left:0;top:674px;width:191px;height:122px;background:var(--paper);display:flex;align-items:center;justify-content:center}
  .partner-box .brand{font-size:18px;color:var(--ink)}

  .callout{left:803px;top:722px;display:flex;align-items:center;color:var(--paper)}
  .callout .brand{font-size:13px;width:122px}
  .callout__rule{width:1.5px;height:56px;background:var(--paper);margin:0 14px}
  .callout__text{font-size:19px;line-height:26px}
  .callout__text b{font-weight:700}
</style>
</head>
<body>

<!-- OUTSIDE SPREAD -->
<section class="spread spread--outside">
  <svg class="spread__art" viewBox="0 0 1133 801" aria-hidden="false">
    <defs>
      <linearGradient id="clubPhoto" x1="0" y1="0" x2="0" y2="1">
        <stop offset="0" stop-color="var(--sky)"/>
        <stop offset=".35" stop-color="var(--foliage)"/>
        <stop offset=".6" stop-color="#6b6f78"/>
        <stop offset="1" stop-color="var(--grass)"/>
      </linearGradient>
      <linearGradient id="paperFold" x1="0" y1="0" x2="1" y2="0">
        <stop offset="0" stop-color="var(--paper-shade)"/>
        <stop offset=".5" stop-color="var(--paper)"/>
        <stop offset="1" stop-color="var(--paper-shade)"/>
      </linearGradient>
    </defs>
    <rect x="0" y="0" width="1133" height="801" fill="url(#paperFold)"/>
    <rect x="280" y="0" width="853" height="560" fill="url(#clubPhoto)" role="img" aria-label="Photo of a lawn bowls clubhouse with palm trees and a green in front"/>
    <!-- white content area under photo -->
    <path d="M377 330 C450 300 600 290 700 330 C760 360 780 440 850 470 C950 510 1050 500 1133 480 V801 H377 Z" fill="url(#paperFold)"/>
    <!-- cover black base -->
    <path d="M755 801 V565 C800 525 880 540 950 560 C1030 582 1090 565 1133 545 V801 Z" fill="var(--ink)"/>
    <path d="M770 505 C820 470 890 495 960 520 C1040 545 1095 530 1133 515" fill="none" stroke="var(--ink)" stroke-width="10"/>
    <!-- intro black panel -->
    <path d="M0 0 H276 C300 0 300 60 320 150 C340 250 360 320 377 330 V801 H0 Z" fill="var(--ink)"/>
    <path d="M270 -5 C300 0 304 60 324 150 C344 245 362 312 392 325" fill="none" stroke="var(--paper)" stroke-width="7"/>
  </svg>

  <div class="abs intro">
    <div class="intro__kicker">OUR WINTERS</div>
    <div class="intro__title">BOWLS TOURS</div>
    <p>offer a chance to join a like-minded group of friends and bowling enthusiasts for the unique lawn bowls experience</p>
    <p>All three tours are fully hosted and include return flights, quality accommodation, numerous groups meals, sightseeing activities, bowls fees plus much more these are a fantastic bowling tours that will truly bowl you over!. Non bowlers are very welcome on all tours as the bowls component is only part the total tour experience.</p>
    <div class="intro__label">Tour Manager and Bowls Ambassador</div>
    <p><span class="intro__name">Peter Holloway</span> is an avid bowler and member of the Kestrel Ridge Bowling Club. Peter has been a European Tour Manager, Cruise Director and is an all-round good guy. Most recently as Silverfern Party Journeys Bowls Ambassador he has help design our last 8 Winter Tours and leads our bowling tours. His experience, assistance, wit and knowledge will ensure that you all have a great deal of fun on tour.</p>
    <div class="intro__heading">SIGHTSEEING &amp; MEALS</div>
    <p>All tours include pre-booked admissions to extensive and diverse range of the most popular sightseeing attractions in all destinations. Along with a number of group meals so the group can enjoy some culinary delights and opportunities to socialise. You're never alone and non-bowlers welcome We know that this Bowling holiday is a great way to meet new people and make new friends so we encourage those travelling solo to join us! Of course, you will have a guaranteed single room when you purchase the single price, however if you prefer not to pay the additional fee, we will match you with another single traveller of the same gender on a shared basis. Occasionally there will be an instance where there are no other single guests and in these cases you will have to pay the single supplement. Whilst we do try our best to match roommates, compatibility cannot be guaranteed and this offer is conditional on acceptance of this factor. Pre or Post Touring We are able to accommodate individuals who are wishing to see more of the destination either before or after the Tour</p>
    <div class="intro__cta">please contact us</div>
    <div>to discuss your touring requirements.</div>
  </div>

  <div class="abs contact">
    <div class="contact__title">CONTACT US TODAY</div>
    <div class="contact__sub">for a more details itinerary on all</div>
    <div class="contact__phones">
      <div class="contact__phone">0800 952 314(Free)</div>
      <div class="contact__phone">027 830 4726(Mobile)</div>
    </div>
    <div class="contact__line">PO Box 51-904 Wellington Mail Centre</div>
    <div class="contact__line">www.silverfernpartyjourneys.example</div>
    <div class="contact__line">bowls@silverfernpartyjourneys.example</div>
    <div class="brand brand--dark contact__brand">Silverfern Party Journeys</div>
  </div>

  <div class="abs cover-logo"><div class="brand brand--light">Silverfern Party Journeys</div></div>

  <div class="abs cover">
    <div class="cover__title">FANTASTIC</div>
    <div class="cover__sub">BOWLING TOURS</div>
    <div class="cover__tag">That will truly bowl you over!</div>
    <div class="cover__url">www.silverfernpartyjourneys.example</div>
  </div>
</section>

<!-- INSIDE SPREAD -->
<section class="spread spread--inside">
  <svg class="spread__art" viewBox="0 0 1133 801">
    <defs>
      <linearGradient id="lakePhoto" x1="0" y1="0" x2="0" y2="1">
        <stop offset="0" stop-color="#b9c9dc"/>
        <stop offset=".35" stop-color="#7d7f78"/>
        <stop offset=".6" stop-color="var(--lake)"/>
        <stop offset="1" stop-color="#4d5e3f"/>
      </linearGradient>
      <linearGradient id="boatPhoto" x1="0" y1="0" x2="1" y2="1">
        <stop offset="0" stop-color="#3a3a3a"/>
        <stop offset=".45" stop-color="var(--boat)"/>
        <stop offset="1" stop-color="var(--spray)"/>
      </linearGradient>
      <linearGradient id="greenPhoto" x1="0" y1="0" x2="0" y2="1">
        <stop offset="0" stop-color="var(--foliage)"/>
        <stop offset=".5" stop-color="#6c7078"/>
        <stop offset="1" stop-color="var(--grass)"/>
      </linearGradient>
      <linearGradient id="paperFold2" x1="0" y1="0" x2="1" y2="0">
        <stop offset="0" stop-color="var(--paper-shade)"/>
        <stop offset=".5" stop-color="var(--paper)"/>
        <stop offset="1" stop-color="var(--paper-shade)"/>
      </linearGradient>
    </defs>
    <rect x="0" y="0" width="1133" height="801" fill="url(#paperFold2)"/>
    <rect x="292" y="0" width="510" height="300" fill="url(#lakePhoto)" role="img" aria-label="Photo of a cable car gondola above a lake town and mountains"/>
    <rect x="749" y="0" width="384" height="300" fill="url(#boatPhoto)" role="img" aria-label="Photo of a jet boat full of cheering passengers throwing spray"/>
    <!-- left panel -->
    <path d="M0 0 H300 C340 0 340 80 377 150 V801 H0 Z" fill="var(--ink)"/>
    <path d="M330 0 C300 0 270 10 250 25 C180 10 90 0 0 25" fill="none" stroke="var(--paper)" stroke-width="6"/>
    <path d="M410 0 C380 20 360 40 340 0" fill="var(--ink)"/>
    <path d="M400 -4 C370 16 350 18 330 -4" fill="none" stroke="var(--paper)" stroke-width="5"/>
    <!-- wave band across photos -->
    <path d="M292 150 C360 140 380 225 470 222 C560 218 600 160 700 172 C780 185 790 255 870 252 C960 248 1050 228 1133 222 V290 C1050 295 960 300 870 300 C790 300 760 290 720 250 C660 200 600 230 540 250 C470 275 400 290 377 270 V150 Z" fill="var(--ink)"/>
    <path d="M377 262 C450 280 520 240 600 212 C680 190 720 250 780 272 C860 298 1000 282 1133 268" fill="none" stroke="var(--paper)" stroke-width="8"/>
    <!-- right panel -->
    <rect x="755" y="290" width="378" height="511" fill="var(--ink)"/>
    <!-- bottom-left club photo -->
    <path d="M0 600 C120 570 250 580 330 650 C380 700 390 760 400 801 H0 Z" fill="url(#greenPhoto)" role="img" aria-label="Photo of a lawn bowls clubhouse and green on the island"/>
    <path d="M0 582 C120 552 262 562 346 638 C398 690 410 755 420 801" fill="none" stroke="var(--paper)" stroke-width="8"/>
  </svg>

  <div class="abs tour tour--light" style="left:47px;top:90px;width:280px">
    <div class="tour__tag">TOUR 1</div>
    <div class="tour__place">NIUE</div>
    <div class="tour__dates">19 JUNE – 27 JUNE 2020</div>
    <div class="tour__about">Niue is a Pacific paradise located north east of New Zealand and is just a 3 ½ hour flight from Auckland. One of the smallest countries, and one of the largest raised coral atolls on earth. Niue is a place where it’s normal for complete strangers to wave at each other, all the time. It’s a place where nature hasn’t been broken… and things are ‘The way they used to be’. Come and enjoy our beautiful little island. Make history and join us on at the first bowls week to held in Niue will included 3 days of bowls on Niue during the week along with a number of sightseeing activities on the Island</div>
    <div class="tour__price-label">PRICE FROM</div>
    <div class="tour__price"><b>$x</b>twin/double share</div>
  </div>

  <div class="abs partner-box"><div class="brand">Coral Isle Visits</div></div>

  <div class="abs tour tour--dark" style="left:438px;top:296px;width:280px">
    <div class="tour__tag">TOUR 2</div>
    <div class="tour__place">NORFOLK ISLAND</div>
    <div class="tour__dates">06 August -14 August 2020</div>
    <div class="tour__about">Norfolk Island is a popular lawn bowls destination, unlike some clubs in Australia and New Zealand the Norfolk greens remain open all year round. With recent reintroduce of direct from New Zealand we are delighted to offer a Tour to Norfolk Island where the locals are very welcoming to New Zealand to their greens. This is the bowls week to held will included 3 days of bowls during the week with a number of sightseeing activities on the island. Also for those wishing to extend onwards we are offering the option to combine with our Golden Sands Tour with a flight from Norfolk to Brisbane</div>
    <div class="tour__price-label">PRICE FROM</div>
    <div class="tour__price"><b>$x</b>twin/double share</div>
  </div>

  <div class="abs tour tour--light" style="left:803px;top:296px;width:280px">
    <div class="tour__tag">TOUR 3</div>
    <div class="tour__place">SUNSHINE COAST</div>
    <div class="tour__dates">15 AUGUST – 23 AUGUST 2020</div>
    <div class="tour__about">The Sunshine Coast our most popular tour with stunning winter climate, so join us for all that Queensland has to offer, this is a fantastic bowling tour that will truly bowl you over! An opportunity for you to experience some special events and enjoy the culture, sights, and foods, wines/beers or course some bowls This bowls week will included 3 days of bowls at different bowls clubs during the week with a number of sightseeing activities on the Sunshine Coast.</div>
    <div class="tour__price-label">PRICE FROM</div>
    <div class="tour__price"><b>$x</b>twin/double share</div>
  </div>

  <div class="abs callout">
    <div class="brand brand--light">Silverfern Party Journeys</div>
    <div class="callout__rule"></div>
    <div class="callout__text">Call Us Today!<br><b>0800 952 314</b></div>
  </div>
</section>

</body>
</html>
```